Bellwood Tax
Project: Business Cards and Stationery
Business Cards and Stationery - Consulting
Business Cards and Stationery
Modern
Peter Marsh
President
28617 Coralind Ave., 4th Floor Sherman Oaks, CA 90572
peterm@bellwdtax.example
www.bellwoodtaxservice.example

```html
<!DOCTYPE html>
<html lang="en">
<head>
<meta charset="utf-8">
<title>Bellwood Tax — Stationery</title>
<link href="https://fonts.googleapis.com/css2?family=Cinzel:wght@500&family=Open+Sans:wght@400;600&display=swap" rel="stylesheet">
<style>
  :root{
    --bg:#eceef0;
    --paper:#ffffff;
    --blue:#3fb8e8;
    --blue-soft:#8fd6f2;
    --ink:#2b2b2b;
    --line:#333333;
    --muted:#8a8f94;
  }
  *{box-sizing:border-box;margin:0;padding:0}
  html,body{width:1200px;height:936px;overflow:hidden;background:var(--bg)}
  .canvas{position:relative;width:1200px;height:936px}
  .piece{position:absolute;background:var(--paper);overflow:hidden;box-shadow:0 2px 6px rgba(0,0,0,.12)}
  .piece svg.wave{position:absolute;inset:0;width:100%;height:100%}
  .brand{position:absolute;display:flex;align-items:center;gap:.45em;font-family:"Cinzel",serif;font-weight:500;color:var(--ink);white-space:nowrap;letter-spacing:.02em}
  .brand .dot{width:1.1em;height:1.1em;border-radius:50%;background:var(--blue);flex:none}
  .fine{position:absolute;font-family:"Open Sans",sans-serif;color:var(--muted);line-height:1.5}
  .contact-list{list-style:none}
  .contact-list li{display:flex;align-items:center;gap:4px}
  .contact-list li::before{content:"";width:5px;height:5px;background:var(--blue);flex:none}
  .faint-circle{position:absolute;border-radius:50%}

  .letterhead{left:182px;top:71px;width:388px;height:541px}
  .folder{left:633px;top:25px;width:500px;height:592px}
  .card-front{left:38px;top:663px;width:202px;height:122px}
  .card-back{left:38px;top:815px;width:202px;height:100px;background:var(--blue)}
  .envelope{left:266px;top:663px;width:430px;height:222px}
  .envelope-back{left:734px;top:663px;width:430px;height:210px}
  .web{position:absolute;left:0;right:0;top:18px;text-align:center;font-family:"Open Sans",sans-serif;font-size:7px;letter-spacing:.25em;color:#fff}
</style>
</head>
<body>
<main class="canvas">

  <section class="piece letterhead" aria-label="Letterhead">
    <svg class="wave" viewBox="0 0 100 100" preserveAspectRatio="none">
      <path d="M0,88 Q62,86 100,57 L100,100 L0,100Z" fill="var(--blue)"/>
      <path d="M0,84.5 Q60,83 100,52.5" fill="none" stroke="var(--line)" stroke-width=".7"/>
    </svg>
    <div class="brand" style="left:22px;top:30px;font-size:15px"><span class="dot"></span>Bellwood Tax</div>
    <ul class="fine contact-list" style="left:264px;top:26px;font-size:5px">
      <li>28617 Coralind Ave., 4th Floor</li>
      <li>Sherman Oaks, CA 90572</li>
      <li>Tel 818 555 0142</li>
      <li>peterm@bellwdtax.example</li>
      <li>www.bellwoodtaxservice.example</li>
    </ul>
    <div class="faint-circle" style="left:134px;top:168px;width:62px;height:62px;background:var(--blue-soft);opacity:.35"></div>
  </section>

  <section class="piece folder" aria-label="Presentation folder">
    <svg class="wave" viewBox="0 0 100 100" preserveAspectRatio="none">
      <path d="M0,96 Q58,95 100,66 L100,100 L0,100Z" fill="var(--blue)"/>
      <path d="M0,93.5 Q57,92 100,62.5" fill="none" stroke="var(--line)" stroke-width=".6"/>
    </svg>
    <div class="faint-circle" style="left:220px;top:210px;width:60px;height:60px;background:var(--blue)"></div>
    <div class="brand" style="left:0;right:0;top:290px;justify-content:center;font-size:36px">Bellwood Tax</div>
  </section>

  <section class="piece card-front" aria-label="Business card front">
    <svg class="wave" viewBox="0 0 100 100" preserveAspectRatio="none">
      <path d="M0,92 Q60,90 100,62 L100,100 L0,100Z" fill="var(--blue)"/>
      <path d="M0,86 Q60,84 100,55" fill="none" stroke="var(--line)" stroke-width="1.2"/>
    </svg>
    <div class="brand" style="left:8px;top:10px;font-size:10px"><span class="dot"></span>Bellwood Tax</div>
    <div class="fine" style="left:10px;top:34px;font-size:4.5px">Peter Marsh<br>President</div>
    <div class="fine" style="left:86px;top:34px;font-size:4.5px">28617 Coralind Ave., 4th Floor<br>Sherman Oaks, CA 90572<br>Tel 818 555 0142<br>peterm@bellwdtax.example</div>
  </section>

  <section class="piece card-back" aria-label="Business card back">
    <div class="faint-circle" style="left:66px;top:6px;width:70px;height:70px;border:10px solid rgba(255,255,255,.35)"></div>
    <div class="brand" style="left:10px;bottom:8px;font-size:10px;color:#fff">Bellwood Tax</div>
  </section>

  <section class="piece envelope" aria-label="Envelope front">
    <svg class="wave" viewBox="0 0 100 100" preserveAspectRatio="none">
      <path d="M0,88 Q58,86 100,40 L100,100 L0,100Z" fill="var(--blue)"/>
      <path d="M0,82 Q57,80 100,33" fill="none" stroke="var(--line)" stroke-width="1"/>
    </svg>
    <div class="brand" style="left:14px;top:14px;font-size:12px"><span class="dot"></span>Bellwood Tax</div>
    <div class="fine" style="left:14px;top:36px;font-size:5px">28617 Coralind Ave., 4th Floor, Sherman Oaks, CA 90572</div>
  </section>

  <section class="piece envelope-back" aria-label="Envelope back">
    <svg class="wave" viewBox="0 0 100 100" preserveAspectRatio="none">
      <path d="M0,0 L100,0 L100,30 Q74,46 53,70 Q50,73 47,70 Q26,46 0,30Z" fill="var(--blue)"/>
    </svg>
    <div class="web">www.bellwoodtaxservice.example</div>
  </section>

</main>
</body>
</html>
```